Highlight Document Over Image for Slide

We are seeking a graphic designer to overlay a news article on an image that pertains to the article, aiming for a stylish yet professional appearance. Given the limited resources, we encourage you to use your imagination and go beyond what basic tools like PowerPoint can offer.

```html
<!DOCTYPE html>
<html lang="en">
<head>
<meta charset="utf-8">
<title>Contraband Policy Highlight</title>
<link rel="stylesheet" href="https://fonts.googleapis.com/css2?family=Tinos:wght@400;700&family=Cousine&display=swap">
<style>
  :root {
    --land-light: #b49a6e;
    --land-mid: #97805c;
    --land-dry: #a88d62;
    --built: #7b7468;
    --built-dark: #6a655c;
    --shore: #6d6a60;
    --water: #5e605a;
    --water-deep: #52544f;
    --paper: #ffffff;
    --fold: #d6d6d6;
    --ink: #1c1c1c;
    --pin-red: #d21c1c;
    --pin-dark: #8e0c0c;
  }
  * { margin: 0; padding: 0; box-sizing: border-box; }
  html, body { width: 1200px; height: 675px; overflow: hidden; background: var(--water); }
  .slide { position: relative; width: 1200px; height: 675px; overflow: hidden; }
  .aerial-map {
    position: absolute; inset: 0;
    background:
      radial-gradient(ellipse 190px 170px at 520px 380px, var(--built-dark) 0%, rgba(106,101,92,0.85) 45%, rgba(106,101,92,0) 100%),
      radial-gradient(ellipse 170px 140px at 200px 230px, rgba(123,116,104,0.9) 0%, rgba(123,116,104,0) 100%),
      radial-gradient(ellipse 260px 110px at 850px 130px, rgba(120,104,80,0.85) 0%, rgba(120,104,80,0) 100%),
      radial-gradient(ellipse 420px 120px at 420px 70px, rgba(180,154,110,0.95) 0%, rgba(180,154,110,0) 100%),
      radial-gradient(ellipse 330px 170px at 1120px 480px, var(--water) 0%, rgba(94,96,90,0.9) 55%, rgba(94,96,90,0) 100%),
      radial-gradient(ellipse 300px 200px at 60px 560px, var(--water-deep) 0%, rgba(82,84,79,0.9) 55%, rgba(82,84,79,0) 100%),
      linear-gradient(180deg, rgba(84,86,80,0) 0%, rgba(84,86,80,0) 78%, var(--water-deep) 96%),
      linear-gradient(170deg, var(--land-light) 0%, var(--land-dry) 18%, var(--land-mid) 34%, var(--built) 50%, var(--shore) 62%, var(--water) 76%, var(--water-deep) 100%);
  }
  .document-note {
    position: absolute; left: 752px; top: 240px; width: 344px; height: 334px;
    filter: drop-shadow(0 3px 6px rgba(0,0,0,0.35));
  }
  .document-sheet {
    position: absolute; inset: 0; background: var(--paper);
    clip-path: polygon(0 0, 100% 0, 100% 100%, 49px 100%, 0 287px);
  }
  .page-fold {
    position: absolute; left: 0; top: 287px; width: 49px; height: 47px;
    background: linear-gradient(135deg, #f4f4f4 0%, var(--fold) 100%);
    clip-path: polygon(0 0, 100% 0, 100% 100%);
  }
  .clause {
    position: absolute; left: 21px; top: 45px; width: 298px;
    font-family: "Tinos", "Times New Roman", serif; color: var(--ink);
  }
  .clause-title {
    display: flex; gap: 0; font-weight: 700; font-size: 14.2px; line-height: 15px;
  }
  .clause-number { width: 22px; flex: none; }
  .clause-body {
    margin: 6px 0 0 22px; width: 274px; font-size: 13.6px; line-height: 15.6px;
  }
  .clause-line { display: block; text-align: justify; text-align-last: justify; white-space: nowrap; }
  .clause-line.last { text-align-last: left; }
  .page-number {
    position: absolute; left: 0; right: 0; top: 278px; text-align: center;
    font-family: "Cousine", monospace; font-size: 11.5px; color: #333;
  }
  .pushpin { position: absolute; left: 918px; top: 212px; width: 46px; height: 62px; }
</style>
</head>
<body>
<div class="slide">
  <div class="aerial-map" role="img" aria-label="Aerial satellite view of a waterfront prison complex with roads, buildings, dry hills and the bay"></div>

  <div class="document-note">
    <div class="document-sheet"></div>
    <div class="page-fold"></div>
    <div class="clause">
      <h2 class="clause-title"><span class="clause-number">20.</span><span>INTRODUCTION OR POSSESSION OF CONTRABAND ITEMS</span></h2>
      <p class="clause-body">
        <span class="clause-line">Employees shall not introduce or possess</span>
        <span class="clause-line">unauthorized items such as escape</span>
        <span class="clause-line">paraphernalia, weapons, facsimiles of weapons,</span>
        <span class="clause-line">ammunition, wireless communication devices,</span>
        <span class="clause-line">cell phones, tobacco or facsimiles of tobacco</span>
        <span class="clause-line">products (e.g. electronic vapor cigarettes),</span>
        <span class="clause-line">lighters or any other item not specifically</span>
        <span class="clause-line">authorized by PD 04.04.100 "Custody, Security</span>
        <span class="clause-line">and Safety Systems (Exempt)", OP 04.04.100</span>
        <span class="clause-line">"Gate Security" or facility operating procedure</span>
        <span class="clause-line">in any facility where offenders are housed.</span>
        <span class="clause-line last">Employees are responsible for any item in their</span>
      </p>
    </div>
    <div class="page-number">36</div>
  </div>

  <svg class="pushpin" viewBox="0 0 46 62" aria-hidden="true">
    <ellipse cx="22" cy="54" rx="13" ry="3.5" fill="rgba(0,0,0,0.18)"/>
    <line x1="16" y1="34" x2="9" y2="52" stroke="#9a9a9a" stroke-width="2.2" stroke-linecap="round"/>
    <path d="M12 30 L26 36 L24 40 Q17 40 12 35 Z" fill="var(--pin-dark)"/>
    <path d="M18 14 L32 20 L27 34 Q19 34 14 28 Z" fill="var(--pin-red)"/>
    <ellipse cx="30" cy="13" rx="11" ry="8" transform="rotate(22 30 13)" fill="var(--pin-red)"/>
    <ellipse cx="27" cy="10" rx="4" ry="2.5" transform="rotate(22 27 10)" fill="#f06a6a"/>
  </svg>
</div>
</body>
</html>
```